Create a banner for me that embodies my health and well being package.

I am an intuitive counselor with a busy practice helping clients to shift their blocks and move forward in their lives.
I have created a package called '9 paths home again'
I am wanting a banner to put on my website page, facebook page and to use as a letter head in mailouts.
My ideal clients are those who want to create change in their lives and who invest money in themselves and their personal and spiritual growth.
I am different to regular life coaches as my sessions have a spiritual twist to them creating much deeper change in my clients.
I would like the banner to be mainly font with the title of the progam: 9 Paths Home Again (no other wording) (something along the lines of the Blackjack font) and that ties in with the theme of my website. I'm not sure what else I want with it and am looking for ideas.
Website:
www.quillorabalancecare.com.au
I also have a current facebook page for the business:
https://www.facebook.com/Quillora-Balance-Care-402715938846102/
(Note: I am about to drop my logo and business name and move to using my own name - the rest of the website will remain the same).
I have attached a doc with the draft of what wording will be on the website page any advertising will link to, to give you an idea of what the program is about.

Target Market(s)

People who invest money on themselves who are looking to improve their emotional well being and creating change in their life. Majority are middle aged women (also younger females and some men)

Industry/Entity Type

Health And Wellness

Font styles to use
Other font styles liked:
• I like Blackjack and Amienne. Along those lines.

Requirements
Must have
• Attractive, modern and GREAT font.
Nice to have
• Surprise me with something amazing!
• I love the colours in the 2 images I have up loaded as they represent the heart chakra colours. They could be a feature on the banner or blurred into the background.
Should not have
• Even though my work is quite spiritual I don't want it to look woo woo (meaning airy fairy spiritual stuff!)

```html
<!DOCTYPE html>
<html lang="en">
<head>
<meta charset="utf-8">
<title>9 Paths Home Again — Banner</title>
<link href="https://fonts.googleapis.com/css2?family=Parisienne&family=Playfair+Display:wght@400&display=swap" rel="stylesheet">
<style>
  :root {
    --leaf-deep: #3f6a22;
    --leaf-mid: #6f9a3a;
    --leaf-light: #9cbd5c;
    --frame-white: #fbfaf6;
    --frame-shadow: rgba(0, 0, 0, 0.28);
    --bloom-pink: #e0579a;
    --band-purple: #6e6c95;
    --band-edge: #abc6a2;
    --title-white: #ffffff;
    --title-sage: #b9d6ad;
  }
  * { box-sizing: border-box; margin: 0; padding: 0; }
  html, body { width: 1200px; height: 628px; overflow: hidden; background: var(--leaf-mid); }
  .banner { position: relative; width: 1200px; height: 628px; overflow: hidden; }

  .backdrop {
    position: absolute; inset: 0;
    background:
      radial-gradient(ellipse 380px 260px at 1080px 380px, #2f5a1c 0%, transparent 70%),
      radial-gradient(ellipse 500px 300px at 150px 120px, var(--leaf-light) 0%, transparent 70%),
      radial-gradient(ellipse 400px 260px at 120px 560px, #35601f 0%, transparent 70%),
      linear-gradient(135deg, var(--leaf-mid), var(--leaf-deep));
  }

  .card { position: absolute; background: var(--frame-white); box-shadow: 0 6px 18px var(--frame-shadow); }
  .card--back { left: 160px; top: 30px; width: 860px; height: 556px; transform: rotate(1.4deg); }
  .card--front { left: 168px; top: 52px; width: 834px; height: 524px; }

  .card__photo {
    position: absolute; left: 24px; top: 26px; width: 786px; height: 472px; overflow: hidden;
    background:
      radial-gradient(ellipse 230px 180px at 460px 170px, var(--bloom-pink) 0%, rgba(224,87,154,0.5) 45%, transparent 75%),
      radial-gradient(ellipse 300px 260px at 700px 300px, #2e5a1e 0%, transparent 70%),
      linear-gradient(160deg, var(--leaf-light) 0%, var(--leaf-mid) 45%, var(--leaf-deep) 100%);
  }

  .title-art { position: absolute; left: 0; top: 0; width: 786px; height: 472px; }

  .title__number {
    font-family: 'Playfair Display', serif; font-size: 230px;
    font-variant-numeric: lining-nums; fill: var(--title-white);
  }
  .title__word { font-family: 'Parisienne', cursive; }
  .title__word--top { font-size: 92px; fill: var(--title-white); }
  .title__word--bottom { font-size: 86px; fill: var(--title-sage); }
</style>
</head>
<body>
  <main class="banner">
    <div class="backdrop" role="img" aria-label="Softly blurred green lotus leaves"></div>

    <div class="card card--back"></div>

    <div class="card card--front">
      <div class="card__photo" role="img" aria-label="Close-up of a pink lotus blossom against green leaves">
        <svg class="title-art" viewBox="0 0 786 472">
          <path d="M0 278 Q 380 160 786 392 L 786 472 L 0 472 Z" fill="var(--band-edge)"/>
          <path d="M0 290 Q 380 178 786 404 L 786 472 L 0 472 Z" fill="var(--band-purple)"/>
          <text class="title__number" x="100" y="427">9</text>
          <text class="title__word title__word--top" x="245" y="335">Paths</text>
          <text class="title__word title__word--bottom" x="228" y="440">Home Again</text>
        </svg>
      </div>
    </div>
  </main>
</body>
</html>
```